The Perfect Business Card for Vantorell

I am looking for a business card which beautifully incorporates my logo, reflects my business and looks special, elegant and clean.

```html
<!DOCTYPE html>
<html lang="en">
<head>
<meta charset="utf-8">
<title>Vantorell Business Card</title>
<link href="https://fonts.googleapis.com/css2?family=Montserrat:wght@400;500;700&display=swap" rel="stylesheet">
<style>
  :root {
    --bg: #e9e9e9;
    --card: #171717;
    --green: #7da33a;
    --white: #f4f4f4;
  }
  * { margin: 0; padding: 0; box-sizing: border-box; }
  html, body { width: 1200px; height: 856px; overflow: hidden; }
  body {
    background: var(--bg);
    font-family: "Montserrat", sans-serif;
    position: relative;
  }
  .card {
    position: absolute;
    top: 273px;
    width: 540px;
    height: 310px;
    background: var(--card);
    border-bottom: 5px solid var(--green);
    color: var(--white);
  }
  .card--front { left: 40px; }
  .card--back  { left: 620px; }

  .brand {
    position: absolute;
    display: flex;
    align-items: center;
    color: var(--green);
    font-weight: 500;
    letter-spacing: 0.06em;
  }
  .brand__dot {
    border: 2px solid var(--green);
    border-radius: 50%;
  }
  .card--front .brand { left: 50%; top: 46px; transform: translateX(-50%); font-size: 34px; gap: 14px; }
  .card--front .brand__dot { width: 46px; height: 46px; }
  .card--back .brand { left: 50%; top: 50%; transform: translate(-50%, -50%); font-size: 44px; gap: 18px; }
  .card--back .brand__dot { width: 62px; height: 62px; }

  .details {
    position: absolute;
    left: 44px; right: 30px; top: 140px;
    display: flex;
    align-items: center;
    gap: 18px;
  }
  .person { text-align: right; flex: 0 0 205px; }
  .person__name { color: var(--green); font-weight: 700; font-size: 17px; letter-spacing: 0.02em; }
  .person__role { font-size: 17px; margin-top: 4px; }
  .divider { width: 1.5px; height: 72px; background: var(--green); }
  .contacts { list-style: none; font-size: 13px; line-height: 1.8; }
  .contacts li { display: flex; align-items: center; gap: 8px; }
  .contacts svg { width: 13px; height: 13px; fill: var(--green); flex: none; }
  .address {
    position: absolute;
    left: 0; right: 0; bottom: 40px;
    text-align: center;
    font-size: 14px;
  }
</style>
</head>
<body>
  <section class="card card--front">
    <div class="brand"><span class="brand__dot"></span>VANTORELL</div>
    <div class="details">
      <div class="person">
        <div class="person__name">DARA WHITCOMBE</div>
        <div class="person__role">Co-Founder</div>
      </div>
      <div class="divider"></div>
      <ul class="contacts">
        <li><svg viewBox="0 0 16 16"><path d="M3.6 1.2l2.3 2.6-1.4 1.9c.9 2 2.4 3.6 4.6 4.8l1.9-1.4 2.6 2.3-1.4 2.4C6.6 13.5 2.4 9.4 1.3 3z"/></svg>(555) 204-7316</li>
        <li><svg viewBox="0 0 16 16"><path d="M1 3h14v10H1z M1.8 3.8L8 9l6.2-5.2" fill="var(--green)" stroke="var(--card)" stroke-width="1.2"/></svg>info@vantorell.com</li>
        <li><svg viewBox="0 0 16 16"><circle cx="8" cy="8" r="7"/><path d="M1 8h14M8 1c-3 3.5-3 10.5 0 14M8 1c3 3.5 3 10.5 0 14" fill="none" stroke="var(--card)" stroke-width="1"/></svg>www.vantorell.com</li>
      </ul>
    </div>
    <p class="address">Ardent Plaza 2150 Mill Crest Ave Suite 310</p>
  </section>

  <section class="card card--back">
    <div class="brand"><span class="brand__dot"></span>VANTORELL</div>
  </section>
</body>
</html>
```